Safety training business card design

We need a buisness card design and logo for a small buisness that provides safety training through out the mining and civil construction industries. We provide first aid , confined space working at heights , machinery tickets, chainsaw, four wheel drive and four wheel motorbike training. We would like to use the design colors of navy blue, Fluro or lime green and white .

Industry/Entity Type

Construction

Contact Information for Business Card

Rillford Groundworks & Training , Neville Ormsby, rillford.skills@mailbox-example.net, ph 0481065374 abn 47 806 315 914

```html
<!DOCTYPE html>
<html lang="en">
<head>
<meta charset="utf-8">
<title>Rillford Groundworks &amp; Training – Business Card</title>
<link rel="stylesheet" href="https://fonts.googleapis.com/css2?family=Tinos:wght@400&display=swap">
<style>
  :root {
    --navy: #22205f;
    --white: #ffffff;
    --mark-faint: #d6d7e6;
    --backdrop: #ecebe8;
    --card-shadow: rgba(0, 0, 0, 0.18);
  }
  * { box-sizing: border-box; margin: 0; padding: 0; }
  html, body {
    width: 1200px;
    height: 1000px;
    overflow: hidden;
  }
  body {
    background: var(--backdrop);
    font-family: "Tinos", "Times New Roman", serif;
    position: relative;
  }
  .card {
    position: absolute;
    left: 290px;
    width: 620px;
    height: 370px;
    border-radius: 14px;
    overflow: hidden;
    box-shadow: 0 6px 18px var(--card-shadow);
  }
  /* Front */
  .card-front {
    top: 60px;
    background: var(--navy);
    color: var(--white);
  }
  .front-mark {
    position: absolute;
    left: 50%;
    top: 78px;
    width: 150px;
    height: 150px;
    margin-left: -75px;
    border-radius: 50%;
    background: var(--white);
  }
  .front-name {
    position: absolute;
    left: 0;
    right: 0;
    top: 262px;
    text-align: center;
    font-size: 27px;
    letter-spacing: 0.2px;
  }
  /* Back */
  .card-back {
    top: 540px;
    background: var(--white);
    color: var(--navy);
  }
  .back-mark {
    position: absolute;
    left: 130px;
    top: 20px;
    width: 360px;
    height: 360px;
    border-radius: 50%;
    border: 60px solid var(--mark-faint);
  }
  .back-heading {
    position: absolute;
    left: 0;
    right: 0;
    top: 64px;
    text-align: center;
    font-size: 26px;
    line-height: 30px;
  }
  .contact-band {
    position: absolute;
    left: 0;
    right: 0;
    top: 172px;
    height: 126px;
    background: var(--navy);
    opacity: 0.97;
    color: var(--white);
    font-size: 26px;
  }
  .contact-item {
    position: absolute;
    display: flex;
    align-items: center;
    gap: 10px;
    white-space: nowrap;
  }
  .contact-abn { left: 60px; top: 28px; }
  .contact-phone { right: 28px; top: 28px; }
  .contact-email { left: 0; right: 0; top: 78px; justify-content: center; font-size: 24px; }
  .abn-badge {
    display: inline-block;
    border: 1.5px solid var(--white);
    border-radius: 5px;
    font-size: 9px;
    padding: 4px 3px;
    line-height: 1;
  }
  .icon { width: 26px; height: 26px; }
</style>
</head>
<body>

  <section class="card card-front" aria-label="Business card front">
    <div class="front-mark"></div>
    <p class="front-name">Rillford Groundworks &amp; Training</p>
  </section>

  <section class="card card-back" aria-label="Business card back">
    <div class="back-mark"></div>
    <p class="back-heading">Rillford Groundworks &amp; Training<br>Neville Ormsby</p>
    <div class="contact-band">
      <div class="contact-item contact-abn">
        <span class="abn-badge">ABN</span>
        <span>47 806 315 914</span>
      </div>
      <div class="contact-item contact-phone">
        <svg class="icon" viewBox="0 0 24 24" aria-hidden="true">
          <path fill="#ffffff" d="M7 2c1 0 2 3 2.3 4.3.2.8-1 1.6-1.4 2.2-.3.5 1.4 3.6 3.4 5.5 1 .9 1.6 1.2 2 .8.6-.6 1.4-1.6 2.2-1.3 1.3.5 4.3 1.6 4.3 2.5 0 1.8-2 4-4 4C9 20 4 13 4 6c0-2 1.7-4 3-4z"/>
        </svg>
        <span>048 106 5374</span>
      </div>
      <div class="contact-item contact-email">
        <svg class="icon" viewBox="0 0 26 20" aria-hidden="true">
          <rect x="1" y="2" width="24" height="16" fill="none" stroke="#ffffff" stroke-width="1.4"/>
          <polyline points="1,2 13,12 25,2" fill="none" stroke="#ffffff" stroke-width="1.4"/>
        </svg>
        <span>rillford.skills@mailbox-example.net</span>
      </div>
    </div>
  </section>

</body>
</html>
```